Executive recruiting firm in need of business card design

Executive recruiting firm looking for a sleek, classy and modern business card design; card itself will be square shape, rounded edges and soft touch paper, our colors are dark blues in the navy color scale, silvers and grays. Reference our website for a better idea of our company's feel and goals at Staffvex.com - our company message is "Employee Engagement Begins at Recruitment" this should be on the card

Industry/Entity Type

Business

```html
<!DOCTYPE html>
<html lang="en">
<head>
<meta charset="utf-8">
<title>Staffvex Business Card</title>
<link href="https://fonts.googleapis.com/css2?family=Open+Sans:wght@400;600;700&display=swap" rel="stylesheet">
<style>
  :root {
    --navy: #1b1d6b;
    --navy-deep: #12144f;
    --navy-light: #262a85;
    --white: #ffffff;
    --ink: #55565c;
    --backdrop: #2b2b2d;
  }
  * { box-sizing: border-box; margin: 0; padding: 0; }
  html, body { width: 1200px; height: 840px; overflow: hidden; }
  body {
    background: var(--backdrop);
    font-family: "Open Sans", Arial, sans-serif;
    position: relative;
  }
  .card {
    position: absolute;
    width: 560px;
    height: 320px;
    border-radius: 14px;
    overflow: hidden;
  }
  .card-front {
    left: 70px; top: 90px;
    background: linear-gradient(135deg, var(--navy-light) 0%, var(--navy) 50%, var(--navy-deep) 100%);
    color: var(--white);
  }
  .brand-name {
    font-weight: 600;
    letter-spacing: 0.5px;
    line-height: 1;
  }
  .card-front .brand-name {
    position: absolute;
    left: 0; right: 0; top: 112px;
    text-align: center;
    font-size: 42px;
    color: var(--white);
  }
  .front-message {
    position: absolute;
    left: 0; right: 0; top: 212px;
    text-align: center;
    font-size: 15px;
    letter-spacing: 0.3px;
  }

  .card-back {
    left: 570px; top: 430px;
    background: var(--white);
  }
  .back-shape { position: absolute; inset: 0; }
  .card-back .brand-name {
    position: absolute;
    left: 40px; top: 72px;
    font-size: 34px;
    color: var(--navy);
  }
  .contact {
    position: absolute;
    left: 40px; top: 150px;
    color: var(--ink);
    font-size: 14px;
    line-height: 20px;
  }
  .contact-address { margin-bottom: 6px; }
  .contact-list { list-style: none; }
  .contact-list li { display: flex; align-items: center; gap: 9px; }
  .contact-list svg { width: 12px; height: 12px; fill: var(--navy); flex: none; }
  .holder {
    position: absolute;
    right: 22px; top: 34px;
    writing-mode: vertical-rl;
    color: var(--white);
    line-height: 20px;
  }
  .holder-name { font-weight: 700; font-size: 14px; letter-spacing: 0.5px; }
  .holder-title { font-weight: 400; font-size: 14px; }
</style>
</head>
<body>

<section class="card card-front">
  <p class="brand-name">Staffvex</p>
  <p class="front-message">Employee Engagement Begins at Recruitment</p>
</section>

<section class="card card-back">
  <svg class="back-shape" viewBox="0 0 560 320" preserveAspectRatio="none" aria-hidden="true">
    <defs>
      <linearGradient id="navyFill" x1="0" y1="0" x2="1" y2="1">
        <stop offset="0" stop-color="#262a85"/>
        <stop offset="1" stop-color="#12144f"/>
      </linearGradient>
    </defs>
    <rect width="560" height="320" fill="url(#navyFill)"/>
    <rect width="250" height="320" fill="#ffffff"/>
    <circle cx="270" cy="250" r="230" fill="#ffffff"/>
  </svg>

  <p class="brand-name">Staffvex</p>

  <div class="contact">
    <p class="contact-address">420 Linden Avenue<br>Maple Grove, CA</p>
    <ul class="contact-list">
      <li><svg viewBox="0 0 12 12"><path d="M2 1h3l1 3-2 1a7 7 0 0 0 3 3l1-2 3 1v3c-6 0-9-3-9-9z"/></svg>555 210 3846</li>
      <li><svg viewBox="0 0 12 12"><rect x="3" y="0.5" width="6" height="11" rx="1"/></svg>555 702 1193</li>
      <li><svg viewBox="0 0 12 12"><rect x="1" y="4" width="10" height="6" rx="1"/><rect x="3" y="1" width="6" height="3"/></svg>555 388 4027</li>
      <li><svg viewBox="0 0 12 12"><path d="M1 2.5h10v7H1z"/></svg>daniel@staffvex.com</li>
      <li><svg viewBox="0 0 12 12"><circle cx="6" cy="6" r="5.5"/></svg>www.staffvex.com</li>
    </ul>
  </div>

  <div class="holder">
    <p class="holder-name">DANIEL REYES</p>
    <p class="holder-title">CEO/FOUNDER</p>
  </div>
</section>

</body>
</html>
```